Medical Services company. Need a website that blows the competition out of the water

We need a web site designed to draw attention to our many services offered. We are a Medical Services business based out of Pennsylvania. We provide basic first aid staffing for events and businesses such as but not limited to: Fairs, Festivals, Carnivals, Sporting events, Large gatherings where a first aid station is needed, Concerts, Businesses with first aid needs . We provide training and certifications that are tailored to the customers needs. We provide Covid-19 pre screening and temperature monitoring. Our professionals consist of individuals with Basic First Aid, Certified Nursing Assistants, Medical Assistants, Emergency Medical Responders (EMR), Emergency Medical Technicians (EMT), and Nurses. I do not know how many pages I will need since we offer multiple different services. Our main services provided are: First Aid services, Covid-19 pre screen and temperatures, and Training/Certifications. You will have to use stock photos for now until I can get some actual photographs of our team.I have uploaded a copy of my brochure so you can get some information from there as well.

Target Market(s)

-For the first Aid and Covid-19 services: All Businesses, Sporting events, Event organizers
-Training: Everyone.

Font styles to use
Sans Serif

Requirements
Must have
• My colors are what is in the logos and Gray , need to have a way for customers to request a quote, design that grabs their attention. Should have pictures of medical providers attending to the sick or injured. Both in a office setting and in an emergency out in public. Should have pictures of an ambulance. Should also have pictures of staff taking temperatures and asking pre screening questions.
Nice to have
• I'll get back to you on that one

```html
<!DOCTYPE html>
<html lang="en">
<head>
<meta charset="utf-8">
<title>Crestline Medical Services</title>
<link rel="stylesheet" href="https://fonts.googleapis.com/css2?family=Cinzel:wght@700&family=Open+Sans:ital,wght@0,400;0,600;0,700;1,400&display=swap">
<style>
:root{
  --navy:#1414a6;
  --navy-deep:#0c0f9c;
  --teal:#17b3a3;
  --violet-top:#7d80d2;
  --violet-bottom:#4a4ec9;
  --service-blue:#3f45b9;
  --paper:#f6f6f6;
  --grey-band:#e6e6e6;
  --text:#555;
  --footer:#232323;
  --footer-text:#d6d6d6;
  --white:#fff;
}
*{box-sizing:border-box;margin:0;padding:0}
html,body{width:1200px;height:3131px;overflow:hidden}
body{font-family:"Open Sans",sans-serif;color:var(--text);background:var(--white);position:relative}
.heading{font-family:"Cinzel",serif;font-weight:700;text-transform:uppercase;letter-spacing:.5px}
section,header,footer{position:absolute;left:0;width:1200px}

/* header */
.site-header{top:0;height:117px;background:var(--white)}
.brand{position:absolute;left:112px;top:30px;display:flex;align-items:center;gap:12px}
.brand-dot{width:46px;height:46px;border-radius:50%;background:var(--navy)}
.brand-name{font-weight:700;font-size:30px;color:var(--navy);letter-spacing:-.5px}
.main-nav{position:absolute;left:420px;top:43px;display:flex;gap:30px;font-size:14.5px;color:#444}
.main-nav a{text-decoration:none;color:inherit;padding-bottom:8px}
.main-nav a.active{color:var(--navy);border-bottom:2px solid var(--navy)}

/* hero */
.hero{top:117px;height:637px;background:radial-gradient(ellipse at 62% 45%,#6a6a72 0%,#3a3940 32%,#1a1a1f 60%,#0d0d10 100%);text-align:center;color:var(--white)}
.hero-title{position:absolute;top:205px;width:100%;font-size:62px;text-shadow:0 2px 6px rgba(0,0,0,.5)}
.hero-sub{position:absolute;top:278px;width:100%;font-size:24px}
.btn-teal{position:absolute;left:523px;top:335px;width:154px;height:49px;border-radius:25px;background:var(--teal);color:var(--white);font-weight:700;font-size:15.5px;line-height:49px;border:2px solid #8fe3d9}
.dots{position:absolute;top:594px;width:100%;display:flex;justify-content:center;gap:9px}
.dots span{width:9px;height:9px;border-radius:50%;background:var(--white)}
.dots span.open{background:none;border:1.5px solid var(--white)}

/* welcome */
.welcome{top:754px;height:498px;background:linear-gradient(180deg,var(--violet-top),var(--violet-bottom))}
.welcome-copy{position:absolute;left:112px;top:80px;width:490px;color:var(--white)}
.welcome-copy h2{font-size:39px;margin-bottom:22px}
.welcome-copy p{font-size:14.5px;line-height:25px;margin-bottom:12px}
.btn-outline-white{display:inline-block;margin-top:24px;width:170px;height:49px;border:2px solid var(--white);border-radius:25px;text-align:center;line-height:45px;font-weight:700;font-size:16px}
.welcome-mark{position:absolute;left:686px;top:62px;width:360px;height:360px;border-radius:50%;background:var(--navy-deep)}

/* professionals */
.professionals{top:1252px;height:572px;background:var(--paper)}
.section-title{position:absolute;width:100%;text-align:center;color:var(--navy);font-size:39px}
.professionals .section-title{top:56px}
.pro-card{position:absolute;top:154px;width:230px;margin-left:-115px;text-align:center}
.pro-icon{width:128px;height:128px;margin:0 auto;border-radius:50%;background:var(--navy);border:5px solid #c7c8e6;display:flex;align-items:center;justify-content:center}
.pro-card h3{height:40px;margin-top:16px;display:flex;align-items:center;justify-content:center;color:var(--navy);font-size:15.5px;font-weight:700;line-height:18px}
.pro-card p{margin-top:5px;font-size:13px;line-height:21.5px}
.btn-outline-navy{display:inline-block;margin-top:16px;width:128px;height:41px;border:2px solid var(--navy);border-radius:21px;line-height:37px;color:var(--navy);font-weight:700;font-size:13.5px}
.arrow{position:absolute;top:210px}

/* services */
.services{top:1824px;height:484px;background:linear-gradient(180deg,#4248bb,var(--service-blue));color:var(--white);text-align:center}
.services .section-title{top:60px;color:var(--white)}
.services-intro{position:absolute;top:112px;left:160px;width:880px;font-size:14.5px;line-height:25px}
.service{position:absolute;top:187px;width:380px;margin-left:-190px}
.service-icon{width:156px;height:156px;margin:0 auto;border-radius:50%;background:var(--white);border:6px solid #b9bce8;display:flex;align-items:center;justify-content:center}
.service h3{margin-top:12px;font-weight:400;font-size:22.5px}

/* testimonials */
.testimonials{top:2308px;height:517px;background:var(--grey-band);text-align:center}
.testimonials .section-title{top:52px}
.client-photo{position:absolute;left:530px;top:111px;width:141px;height:141px;border-radius:50%;background:linear-gradient(135deg,#e9d2a6,#b98a5c);border:4px solid var(--white)}
.quote{position:absolute;left:190px;top:272px;width:820px;font-style:italic;font-size:16px;line-height:23.5px}
.quote-mark{position:absolute;font-family:Georgia,serif;font-size:56px;color:#b5b5b5;line-height:1}
.client-name{position:absolute;top:373px;width:100%;color:var(--teal);font-family:"Cinzel",serif;font-size:18px;font-weight:700}
.testimonials .dots{top:443px}
.testimonials .dots span{width:7px;height:7px;background:#c9c9c9}
.testimonials .dots span.on{background:var(--navy)}

/* footer */
.site-footer{top:2825px;height:306px;background:var(--footer);color:var(--footer-text)}
.footer-title{position:absolute;top:46px;color:var(--white);font-weight:700;font-size:16px}
.link-col{position:absolute;top:96px;list-style:none;font-size:13px}
.link-col li{height:30.5px}
.contact-list{position:absolute;left:550px;top:96px;list-style:none}
.contact-list li{display:flex;gap:12px;align-items:flex-start;margin-bottom:14px}
.contact-list .small{font-size:12px;line-height:17px}
.contact-list .big{font-size:15.5px;font-weight:600;color:var(--white)}
.social{position:absolute;left:920px;top:100px;display:flex;gap:8px}
.social span{width:36px;height:36px;border:2px solid #bbb;border-radius:50%}
.badge{position:absolute;left:918px;top:155px;width:52px;height:52px;border-radius:50%;background:#3a4fa0}
.footer-rule{position:absolute;left:112px;top:251px;width:976px;height:1px;background:#444}
.copyright{position:absolute;left:112px;top:270px;font-size:12.5px;color:var(--white)}
.legal{position:absolute;right:112px;top:270px;font-size:10.5px;color:#aaa}
</style>
</head>
<body>

<header class="site-header">
  <div class="brand"><span class="brand-dot"></span><span class="brand-name">Crestline</span></div>
  <nav class="main-nav">
    <a class="active">HOME</a><a>ABOUT US</a><a>OUR PROFESSIONALS</a><a>CRESTLINE SERVICES</a><a>OUR TEAM</a><a>CONTACT US</a>
  </nav>
</header>

<section class="hero" role="img" aria-label="Paramedic wheeling a stretcher beside an ambulance at night">
  <h1 class="heading hero-title">Crestline Medical Services</h1>
  <p class="hero-sub">We are Medical Professionals providing you with professional services</p>
  <div class="btn-teal">CONTACT US</div>
  <div class="dots"><span class="open"></span><span></span><span></span><span></span></div>
</section>

<section class="welcome">
  <div class="welcome-copy">
    <h2 class="heading">Welcome to Crestline</h2>
    <p>Lorem ipsum dolor sit amet, consectetur adipiscing elit, sed do eiusmod tempor incididunt ut labore et dolore magna aliqua. Ut enim ad minim veniam, quis nostrud exercitation ullamco laboris nisi ut aliquip ex ea commodo consequat.</p>
    <p>Sed ut perspiciatis unde omnis iste natus error sit voluptatem accusantium doloremque laudantium, totam rem aperiam, eaque ipsa quae ab illo inventore veritatis et quasi architecto beatae vitae dicta sunt explicabo</p>
    <div class="btn-outline-white">LEARN MORE</div>
  </div>
  <div class="welcome-mark"></div>
</section>

<section class="professionals">
  <h2 class="heading section-title">Our Professionals</h2>
  <svg class="arrow" style="left:46px" width="24" height="44" viewBox="0 0 24 44"><path d="M20 4 4 22l16 18" fill="none" stroke="#aaa" stroke-width="4"/></svg>
  <svg class="arrow" style="left:1118px" width="24" height="44" viewBox="0 0 24 44"><path d="M4 4l16 18L4 40" fill="none" stroke="#aaa" stroke-width="4"/></svg>

  <div class="pro-card" style="left:221px">
    <div class="pro-icon"><svg width="60" height="44" viewBox="0 0 60 44" fill="none" stroke="#fff" stroke-width="3"><rect x="4" y="6" width="36" height="26" rx="3"/><path d="M40 14h8l8 10v8H40z"/><circle cx="16" cy="36" r="5"/><circle cx="46" cy="36" r="5"/><path d="M22 13v12M16 19h12" stroke="#ff5a6e"/></svg></div>
    <h3>EMERGENCY MEDICAL TECHNICIANS (EMT)</h3>
    <p>Temporibus autem quibusdam et aut officiis debitis aut rerum saepe eveniet ut et voluptates sint et molestiae non recusandae earum rerum hic tenetur a sapiente reiciendis voluptatibus.</p>
    <div class="btn-outline-navy">LEARN MORE</div>
  </div>
  <div class="pro-card" style="left:474px">
    <div class="pro-icon"><svg width="56" height="60" viewBox="0 0 56 60" fill="none" stroke="#fff" stroke-width="3"><path d="M36 4c-6 0-8 4-8 10v14c0 6 4 10 10 10s10-4 10-10V14c0-6-2-10-8-10"/><path d="M38 38v6c0 8-6 12-14 12S10 52 10 44"/><circle cx="10" cy="36" r="8"/><path d="M10 31v10M5 36h10" stroke="#ff5a6e"/></svg></div>
    <h3>CERTIFIED NURSING ASSISTANTS</h3>
    <p>Temporibus autem quibusdam et aut officiis debitis aut rerum saepe eveniet ut et voluptates sint et molestiae non recusandae earum rerum hic tenetur a sapiente reiciendis voluptatibus.</p>
    <div class="btn-outline-navy">LEARN MORE</div>
  </div>
  <div class="pro-card" style="left:726px">
    <div class="pro-icon"><svg width="52" height="62" viewBox="0 0 52 62" fill="none" stroke="#fff" stroke-width="3"><path d="M14 6h24v12H14z"/><path d="M26 8v8M22 12h8" stroke="#ff5a6e"/><path d="M14 18v6a12 12 0 0 0 24 0v-6"/><path d="M4 60V48c0-6 8-10 14-10h16c6 0 14 4 14 10v12z"/></svg></div>
    <h3>MEDICAL ASSISTANTS</h3>
    <p>Temporibus autem quibusdam et aut officiis debitis aut rerum saepe eveniet ut et voluptates sint et molestiae non recusandae earum rerum hic tenetur a sapiente reiciendis voluptatibus.</p>
    <div class="btn-outline-navy">LEARN MORE</div>
  </div>
  <div class="pro-card" style="left:978px">
    <div class="pro-icon"><svg width="56" height="58" viewBox="0 0 56 58" fill="none" stroke="#fff" stroke-width="3"><path d="M10 20c0-12 8-16 18-16s18 4 18 16z"/><path d="M28 8v8M24 12h8" stroke="#ff5a6e"/><path d="M10 20v12c0 14 8 22 18 22s18-8 18-22V20"/></svg></div>
    <h3>REGISTERED NURSES</h3>
    <p>Temporibus autem quibusdam et aut officiis debitis aut rerum saepe eveniet ut et voluptates sint et molestiae non recusandae earum rerum hic tenetur a sapiente reiciendis voluptatibus.</p>
    <div class="btn-outline-navy">LEARN MORE</div>
  </div>
</section>

<section class="services" role="img" aria-label="Blue-tinted hospital ward with beds in the background">
  <h2 class="heading section-title">Our Main Services</h2>
  <p class="services-intro">But I must explain to you how all this mistaken idea of denouncing pleasure and praising pain was born and I will give you a complete account of the system, and expound the actual teachings of the great explorer of the truth, the master-builder of human happiness.</p>
  <div class="service" style="left:238px">
    <div class="service-icon"><svg width="80" height="64" viewBox="0 0 80 64" fill="none" stroke="#2a33a8" stroke-width="3"><rect x="4" y="14" width="72" height="46" rx="2"/><path d="M28 14V6h24v8"/><path d="M34 26h12v8h8v12h-8v8H34v-8h-8V34h8z" stroke="#ff5a6e"/></svg></div>
    <h3>First Aid Services</h3>
  </div>
  <div class="service" style="left:575px">
    <div class="service-icon"><svg width="60" height="90" viewBox="0 0 60 90" fill="none" stroke="#2a33a8" stroke-width="3"><path d="M18 60V14a8 8 0 0 1 16 0v46a14 14 0 1 1-16 0z"/><circle cx="26" cy="72" r="5"/><path d="M26 67V34M34 26h6M34 36h6M34 46h6"/><path d="M50 4v14M43 11h14" stroke="#ff5a6e"/></svg></div>
    <h3>Covid-19 Pre Screen and Temperatures</h3>
  </div>
  <div class="service" style="left:934px">
    <div class="service-icon"><svg width="76" height="90" viewBox="0 0 76 90" fill="none" stroke="#2a33a8" stroke-width="3"><circle cx="38" cy="34" r="26"/><circle cx="38" cy="34" r="18"/><path d="M30 34l6 6 12-12" stroke="#ff5a6e"/><path d="M22 54 12 80l10-4 6 8 8-24M54 54l10 26-10-4-6 8-8-24"/></svg></div>
    <h3>Training/Certifications</h3>
  </div>
</section>

<section class="testimonials">
  <h2 class="heading section-title">Client Testimonials</h2>
  <div class="client-photo" role="img" aria-label="Portrait photo of a smiling couple outdoors"></div>
  <span class="quote-mark" style="left:162px;top:256px">&ldquo;</span>
  <p class="quote">At vero eos et accusamus et iusto odio dignissimos ducimus qui blanditiis praesentium voluptatum deleniti atque corrupti quos dolores et quas molestias excepturi sint occaecati cupiditate non provident, similique sunt in culpa qui officia deserunt mollitia animi, id est laborum et dolorum fuga. Et harum quidem rerum facilis est et expedita distinctio</p>
  <span class="quote-mark" style="left:994px;top:318px">&rdquo;</span>
  <div class="client-name">DANA WHITFIELD-ROSS</div>
  <div class="dots"><span class="on"></span><span></span><span></span><span></span></div>
</section>

<footer class="site-footer">
  <h4 class="footer-title" style="left:112px">QUICK LINKS</h4>
  <ul class="link-col" style="left:112px"><li>Home</li><li>About Us</li><li>Our Professionals</li><li>Main Services</li></ul>
  <ul class="link-col" style="left:343px"><li>Site Map</li><li>Blog</li><li>Testimonials</li><li>Contact Us</li></ul>

  <h4 class="footer-title" style="left:550px">CONTACT US</h4>
  <ul class="contact-list">
    <li><svg width="12" height="17" viewBox="0 0 12 17"><path d="M6 0a6 6 0 0 0-6 6c0 5 6 11 6 11s6-6 6-11a6 6 0 0 0-6-6z" fill="#fff"/><circle cx="6" cy="6" r="2.3" fill="#232323"/></svg><span class="small">Crestline Medical Services, Street Address,<br>City Name, Country code.</span></li>
    <li><svg width="16" height="16" viewBox="0 0 16 16"><path d="M3 1l3 3-2 2c1 2 4 5 6 6l2-2 3 3-2 2C7 15 1 9 1 3z" fill="#fff"/></svg><span class="big">555-014-2290</span></li>
    <li><svg width="20" height="15" viewBox="0 0 20 15"><rect width="20" height="15" rx="1" fill="#fff"/><path d="M1 1l9 7 9-7" fill="none" stroke="#232323" stroke-width="1.6"/></svg><span class="big">care@crestlinemed.example</span></li>
  </ul>

  <h4 class="footer-title" style="left:914px">CONNECT WITH US</h4>
  <div class="social"><span></span><span></span><span></span><span></span></div>
  <div class="badge"></div>

  <div class="footer-rule"></div>
  <p class="copyright">Copyrights &copy; 2020 Crestline Medical Services. All rights reserved.</p>
  <p class="legal">Terms and Conditions | Privacy Policy</p>
</footer>

</body>
</html>
```